Tarrow Creek plumbing plumbing company business card design

Something sinilar to business card i upload it is my old business card design
And have a good watermark with the logo or majority of the logot in rhe background as watermark

Plumbing business similar to uploaded design with a nice watermark of the logo

Font styles to use
Script

Colors

Designer to choose colors to be used in the design.

```html
<!DOCTYPE html>
<html lang="en">
<head>
<meta charset="utf-8">
<title>Tarrow Creek Plumbing – Business Card</title>
<link href="https://fonts.googleapis.com/css2?family=Arimo:wght@400;700&family=Montserrat:wght@600;800&display=swap" rel="stylesheet">
<style>
  :root {
    --stage: #e9e6e1;
    --blue-light: #12b4e6;
    --blue-dark: #0a86c4;
    --pipe-pale: #c9d8ee;
    --ink: #111111;
    --white: #ffffff;
    --black-card: #050505;
    --pipe-faint: #262626;
    --accent: #1ea6df;
  }
  * { box-sizing: border-box; margin: 0; padding: 0; }
  html, body { width: 1200px; height: 780px; overflow: hidden; }
  body {
    background: var(--stage);
    font-family: "Arimo", Arial, sans-serif;
    position: relative;
  }
  .card {
    position: absolute;
    top: 215px;
    width: 525px;
    height: 300px;
    border-radius: 4px;
    overflow: hidden;
    box-shadow: 0 10px 26px rgba(0,0,0,.18);
  }
  /* Front */
  .card--front {
    left: 50px;
    background: radial-gradient(ellipse at 75% 35%, var(--blue-light), var(--blue-dark) 95%);
  }
  .front__watermark {
    position: absolute;
    left: 0; bottom: 0;
    width: 270px; height: 170px;
    border-radius: 0 60px 0 0;
    background: linear-gradient(160deg, var(--pipe-pale), #b9cbe6);
    opacity: .9;
  }
  .front__brand {
    position: absolute;
    right: 34px; top: 28px;
    text-align: right;
  }
  .brand-name {
    font-family: "Montserrat", sans-serif;
    font-weight: 800;
    font-size: 26px;
    letter-spacing: 1px;
    color: var(--ink);
    text-transform: uppercase;
    line-height: 1.1;
  }
  .front__person {
    position: absolute;
    right: 34px; top: 104px;
    text-align: right;
  }
  .person-name {
    font-weight: 700;
    font-size: 22px;
    line-height: 1.15;
    color: var(--ink);
  }
  .person-rule {
    width: 150px; height: 2px;
    background: var(--white);
    margin: 6px 0 5px auto;
  }
  .person-role {
    font-size: 13px;
    line-height: 1.2;
    color: var(--white);
  }
  .front__contact {
    position: absolute;
    right: 34px; bottom: 18px;
    list-style: none;
    color: var(--white);
    font-size: 12.5px;
    line-height: 1.45;
  }
  .front__contact li { display: flex; align-items: center; gap: 7px; }
  .front__contact .no-icon { padding-left: 17px; }
  .front__contact svg { width: 10px; height: 10px; fill: var(--white); flex: none; }

  /* Back */
  .card--back {
    right: 50px;
    background: var(--black-card);
  }
  .back__watermark {
    position: absolute;
    left: 40px; top: 0;
    width: 300px; height: 200px;
    border-radius: 0 0 90px 0;
    background: linear-gradient(160deg, #2c2c2c, var(--pipe-faint));
  }
  .back__brand {
    position: absolute;
    right: 36px; bottom: 40px;
    display: flex;
    align-items: center;
    gap: 12px;
  }
  .back__brand .brand-name { color: var(--white); font-size: 24px; }
  .brand-dot {
    width: 16px; height: 16px;
    border-radius: 50%;
    background: var(--accent);
  }
</style>
</head>
<body>

  <section class="card card--front" aria-label="Card front">
    <div class="front__watermark" role="img" aria-label="Large faint pipe and tap watermark"></div>

    <div class="front__brand">
      <p class="brand-name">Tarrow Creek<br>Plumbing</p>
    </div>

    <div class="front__person">
      <p class="person-name">Dana Whitlock</p>
      <div class="person-rule"></div>
      <p class="person-role">Director</p>
    </div>

    <ul class="front__contact">
      <li class="no-icon">PO Box 48, Creek Road</li>
      <li class="no-icon">2nd Street Tarrow</li>
      <li><svg viewBox="0 0 10 10"><path d="M2 0h2l1 3-1.5 1a6 6 0 0 0 2.5 2.5L7 5l3 1v2c0 1-1 2-2 2A8 8 0 0 1 0 2c0-1 1-2 2-2z"/></svg>0400 555 019</li>
      <li><svg viewBox="0 0 10 10"><path d="M0 2h10v6H0z M0 2l5 3.5L10 2" fill="none" stroke="#fff" stroke-width="1.2"/></svg>info@tarrowcreek.com</li>
      <li><svg viewBox="0 0 10 10"><circle cx="5" cy="5" r="4.4" fill="none" stroke="#fff" stroke-width="1"/><path d="M0.6 5h8.8M5 0.6v8.8" stroke="#fff" stroke-width=".8"/></svg>www.tarrowcreek.com</li>
    </ul>
  </section>

  <section class="card card--back" aria-label="Card back">
    <div class="back__watermark" role="img" aria-label="Large dark pipe and tap watermark"></div>
    <div class="back__brand">
      <span class="brand-dot"></span>
      <p class="brand-name">Tarrow Creek<br>Plumbing</p>
    </div>
  </section>

</body>
</html>
```